dessert restaurant

I need a business card design for my restaurant. It will primarily be a dessert and wine restaurant. I will serve delicious baked from scratch desserts, cake, pies cookies brownies etc. Select red and white wines.I will also offer light breakfast, and lunch menu. This will be an upscale contemporary design restaurant with reasonably priced items on the menu. I will also offer small plates in the evening with dessert menu. my color scheme is cobalt blue , red, white black. My restaurant will be the place where adults come after enjoying the meal at a restaurant and want to enjoy a dessert and a glass of wine to finish off their evening. I will also have contemporary jazz sounds for atmosphere.

Industry/Entity Type

Restaurant

Contact Information for Business Card

delia marsh 415 862 3094

```html
<!DOCTYPE html>
<html lang="en">
<head>
<meta charset="utf-8">
<title>Velour — Business Card</title>
<link rel="stylesheet" href="https://fonts.googleapis.com/css2?family=Crimson+Text:wght@400;600;700&display=swap">
<style>
  :root {
    --backdrop: #d8d9dc;
    --card: #ffffff;
    --cobalt: #0047ab;
    --cobalt-deep: #003a8c;
    --red: #c8102e;
    --ink: #111111;
  }
  * { margin: 0; padding: 0; box-sizing: border-box; }
  html, body {
    width: 1200px;
    height: 960px;
    overflow: hidden;
    background: var(--backdrop);
  }
  .canvas {
    width: 1200px;
    height: 960px;
    display: flex;
    align-items: center;
    justify-content: center;
  }
  .business-card {
    position: relative;
    width: 500px;
    height: 820px;
    background: var(--card);
    box-shadow: 0 10px 30px rgba(0,0,0,0.18);
    font-family: "Crimson Text", Georgia, serif;
    color: var(--cobalt);
    text-align: center;
    overflow: hidden;
  }
  .brand {
    position: absolute;
    top: 110px;
    left: 0;
    right: 0;
    font-size: 72px;
    font-weight: 600;
    letter-spacing: 4px;
    line-height: 1;
    color: var(--cobalt);
  }
  .holder {
    position: absolute;
    top: 330px;
    left: 0;
    right: 0;
  }
  .holder-name {
    font-size: 40px;
    font-weight: 700;
    letter-spacing: 1px;
    line-height: 1.1;
    color: var(--cobalt);
  }
  .holder-title {
    display: inline-block;
    font-size: 22px;
    font-weight: 400;
    letter-spacing: 0.5px;
    padding: 0 14px 6px;
    color: var(--ink);
    border-bottom: 2px solid var(--red);
  }
  .contact {
    position: absolute;
    top: 500px;
    left: 0;
    right: 0;
    list-style: none;
    font-size: 27px;
    font-weight: 700;
    line-height: 1.22;
    color: var(--ink);
  }
  .footer-band {
    position: absolute;
    left: 0;
    right: 0;
    bottom: 0;
    height: 98px;
    background: var(--cobalt-deep);
  }
  .footer-band::before {
    content: "";
    position: absolute;
    left: 0;
    right: 0;
    top: 12px;
    height: 3px;
    background: var(--red);
  }
</style>
</head>
<body>
<main class="canvas">
  <section class="business-card">
    <h1 class="brand">VELOUR</h1>
    <div class="holder">
      <p class="holder-name">Delia Marsh</p>
      <p class="holder-title">Managing Director</p>
    </div>
    <ul class="contact">
      <li>415 862 3094</li>
      <li>www.velourdesserts.com</li>
      <li>1187 Harlow St. N.W. Wash</li>
      <li>D.C. 20009</li>
    </ul>
    <div class="footer-band"></div>
  </section>
</main>
</body>
</html>
```